Harlow Consulting, Business Cards for International Development Consultancy

I'm an independent consultant working in the international development sector. I work with small organisations in developing countries to help them develop their community based programs so that they can be internationally competitive. This means they need to work better with their own communities to deliver meaningful quality work and also improve the accountability of their work so that they can compete for international and domestic funding.

I like the idea of being a connector between community, local organisations and international best practice and back again (ie acknowledging that international best practice can learn a lot from community).

My surname is Harlow - so I'd like the logo to use the idea of web as a connector.

I work with people with sight impairments - would like my card to be useful for low vision (i.e. clear graphics, easy to read font) and no vision (i.e. brail).

Target Market(s)

international non-government organisations (i.e. corvane, lift the villages, brightpath aid), Blue Harbour Green Lantern, government (i.e. Australian Bureau of Overseas Partnerships, consulars), non government agencies,

Industry/Entity Type

Business

Contact Information for Business Card

International Development Consultant
Connecting International Development with Community

Mirela Harlow
Lead Consultant
Phone: +61 412 558127
Email: mharlow.consulting@quillmail.net

Font styles to use
Sans Serif

Colors
eaf1f7
85acd3
d3a5cc
0456a4
a64599
0255a3

Requirements
Nice to have
• brail
Should not have
• fancy fonts - needs to be easy to read.

```html
<!DOCTYPE html>
<html lang="en">
<head>
<meta charset="utf-8">
<title>Harlow Consulting — Business Cards</title>
<link rel="stylesheet" href="https://fonts.googleapis.com/css2?family=Questrial&display=swap">
<style>
  :root {
    --backdrop: #ececea;
    --card-dark: #1d1c1e;
    --card-magenta: #a3249b;
    --magenta: #b02aa6;
    --ink: #222222;
    --paper-white: #f2f2f2;
    --muted-white: #e4e4e4;
  }
  * { box-sizing: border-box; margin: 0; padding: 0; }
  html, body {
    width: 1200px; height: 1021px; overflow: hidden;
    background: var(--backdrop);
    font-family: "Questrial", "Century Gothic", sans-serif;
  }
  .sheet { position: relative; width: 1200px; height: 1021px; }

  .card {
    position: absolute; width: 500px; height: 305px;
    border-radius: 4px;
    box-shadow: 0 10px 24px rgba(0,0,0,0.18);
  }
  .card--back { left: 90px; top: 120px; background: var(--card-dark); }
  .card--front { left: 620px; top: 420px; background: var(--card-magenta); }

  .brand { display: flex; align-items: center; gap: 12px; position: absolute; }
  .brand__square { display: block; flex: none; }
  .brand__name { white-space: nowrap; line-height: 1; }

  .card--back .brand { right: 30px; top: 34px; }
  .card--back .brand__square { width: 22px; height: 22px; background: var(--magenta); }
  .card--back .brand__name { font-size: 26px; color: var(--paper-white); }

  .contact { position: absolute; left: 36px; bottom: 34px; color: var(--paper-white); }
  .contact__name { font-size: 26px; margin-bottom: 4px; }
  .contact__role { font-size: 13px; color: var(--magenta); margin-bottom: 16px; }
  .contact__line { display: flex; align-items: center; gap: 10px; font-size: 16px; margin-top: 8px; color: var(--muted-white); }
  .contact__icon { width: 16px; height: 16px; flex: none; }

  .card--front .brand { left: 50%; top: 50%; transform: translate(-50%, -50%); gap: 16px; }
  .card--front .brand__square { width: 34px; height: 34px; background: var(--card-dark); }
  .card--front .brand__name { font-size: 40px; color: var(--paper-white); }

  .lockup { left: 80px; top: 830px; gap: 20px; }
  .lockup .brand__square { width: 52px; height: 52px; background: var(--magenta); }
  .lockup .brand__name { font-size: 58px; color: var(--ink); }
</style>
</head>
<body>
<main class="sheet">

  <section class="card card--back" aria-label="Business card back">
    <div class="brand">
      <span class="brand__square"></span>
      <span class="brand__name">Harlow Consulting</span>
    </div>
    <div class="contact">
      <p class="contact__name">Mirela Harlow</p>
      <p class="contact__role">Lead Consultant</p>
      <p class="contact__line">
        <svg class="contact__icon" viewBox="0 0 16 16" aria-hidden="true">
          <rect x="1" y="3" width="14" height="10" fill="none" stroke="#b02aa6" stroke-width="1.6"/>
          <path d="M1 3 L8 9 L15 3" fill="none" stroke="#b02aa6" stroke-width="1.6"/>
        </svg>
        +61 412 558127
      </p>
      <p class="contact__line">
        <svg class="contact__icon" viewBox="0 0 16 16" aria-hidden="true">
          <path d="M2 5 Q8 1 14 5 L12 7 L10 5.5 L6 5.5 L4 7 Z" fill="#b02aa6"/>
          <rect x="3" y="8" width="10" height="6" rx="1" fill="#b02aa6"/>
        </svg>
        mharlow.consulting@quillmail.net
      </p>
    </div>
  </section>

  <section class="card card--front" aria-label="Business card front">
    <div class="brand">
      <span class="brand__square"></span>
      <span class="brand__name">Harlow Consulting</span>
    </div>
  </section>

  <div class="brand lockup">
    <span class="brand__square"></span>
    <span class="brand__name">Harlow Consulting</span>
  </div>

</main>
</body>
</html>
```